Design für Digitalisierungsprojekte
Zielgruppe
Wir sind der digitale Problemlöser, d.h. wir machen Digitalisierungsprojekte, von der Strategieberatung bis zur technischen Umsetzung und dem Kulturwandel. Wir machen individuelle Projekte, keine Produkte von der Stange. Unsere Kunden sind gehobener Mittelstand bis Konzern, ab 25 Mio € aufwärts. Oft sind unsere Kunden aus konservativen Branchen. Wir müssen beim Design immer einen Kompromiss aus innovativ und Vertrauen erweckend finden.
Aufgabenstellung
E-Book Design
Exo2 und open sans ist unsere Schriftart. Logos habe ich in 2 Formaten angehängt.
Auf den beiden Flyern angehängt finden Sie die Corporate Identity.
Ebook Inhalt ist im Anhang als Word Datei
Wenn Sie weitere Ideen haben, sind wir ganz Ohr.
Grafisch bitte nur die Farben grau, schwarz und orange verwenden (grau und orange siehe Logo)

```html
<!DOCTYPE html>
<html lang="de">
<head>
<meta charset="utf-8">
<title>Sicherheit in LoRaWAN Netzen – E-Book</title>
<link rel="stylesheet" href="https://fonts.googleapis.com/css2?family=Exo+2:wght@400;600;700;800&family=Open+Sans:wght@400;600;700&display=swap">
<style>
:root{
  --orange:#e8731e;
  --grey:#8c8c8c;
  --grey-dark:#6e6e6e;
  --grey-light:#d6d6d6;
  --ink:#333333;
  --paper:#ffffff;
  --stage:#ececec;
}
*{box-sizing:border-box;margin:0;padding:0}
html,body{width:1200px;height:4012px;overflow:hidden;background:var(--stage)}
body{font-family:"Open Sans",sans-serif;color:var(--ink);position:relative}
.sheet{position:absolute;left:0;width:1200px;height:802px}
.page{position:absolute;top:19px;width:540px;height:764px;background:var(--paper);box-shadow:0 2px 10px rgba(0,0,0,.12);overflow:hidden}
.spread .page.left{left:60px}
.spread .page.right{left:600px;box-shadow:2px 2px 10px rgba(0,0,0,.12)}
.spread .page.left::after{content:"";position:absolute;right:0;top:0;width:30px;height:100%;background:linear-gradient(to right,rgba(0,0,0,0),rgba(0,0,0,.06))}
.spread .page.right::before{content:"";position:absolute;left:0;top:0;width:30px;height:100%;background:linear-gradient(to left,rgba(0,0,0,0),rgba(0,0,0,.06))}
.cover-sheet .page{left:330px}
.brand{font-family:"Exo 2",sans-serif;font-weight:700;color:var(--orange);letter-spacing:3px;display:flex;align-items:center;gap:6px}
.brand .dot{width:8px;height:8px;border-radius:50%;background:var(--orange)}
.brand-tag{font-family:"Open Sans",sans-serif;font-size:6px;letter-spacing:1px;color:var(--grey);text-transform:uppercase;margin-top:2px}
.title-small{font-family:"Exo 2",sans-serif;font-weight:700;color:var(--ink)}
.title-big{font-family:"Exo 2",sans-serif;font-weight:800;color:var(--orange);line-height:.95}
.body-text{font-size:9.3px;line-height:1.6;text-align:justify}
.body-text p{margin-bottom:10px}
.folio{position:absolute;bottom:30px;left:50px;right:50px;display:flex;align-items:center;gap:10px;font-size:7px;color:var(--grey);letter-spacing:1px}
.folio .rule{flex:1;height:3px;background:var(--grey-light)}
.page.right .folio{flex-direction:row-reverse}
.chapter-head{display:flex;gap:12px;align-items:flex-start}
.chapter-num{flex:0 0 30px;height:30px;border-radius:50%;background:var(--grey);color:#fff;font-family:"Exo 2",sans-serif;font-weight:700;font-size:12px;display:flex;align-items:center;justify-content:center;margin-top:6px}
.chapter-title{font-family:"Exo 2",sans-serif;font-weight:700;color:var(--orange);font-size:19px;line-height:1.15}
.lead{font-weight:700;font-size:9.5px;line-height:1.55;margin:14px 0 10px}
.bullets{list-style:none;font-size:9.3px;line-height:1.6}
.bullets li{position:relative;padding-left:16px;margin-bottom:7px;text-align:justify}
.bullets li::before{content:"";position:absolute;left:2px;top:5px;width:6px;height:6px;border-radius:50%;background:var(--orange)}
.alpha{list-style:none;font-size:9.3px;line-height:1.6}
.alpha li{position:relative;padding-left:18px;margin-bottom:7px}
.alpha li span{position:absolute;left:0;color:var(--orange);font-weight:700}
.corner-block{position:absolute;top:0;width:42px;height:80px}
/* cover */
.cover-photo{position:absolute;left:110px;top:0;right:0;height:420px;background:linear-gradient(135deg,#0d2a55 0%,#1d5fa8 45%,#4aa3dd 75%,#0b1f40 100%)}
.cover-title-box{position:absolute;left:230px;top:330px;width:280px;height:160px;background:#fff;padding:22px 22px}
.cover-title-box .title-small{font-size:22px}
.cover-title-box .title-big{font-size:38px;margin:4px 0}
.cover-underline{width:90px;height:5px;background:var(--orange);margin-top:8px}
.cover-author{position:absolute;left:240px;top:560px;font-size:9.5px;line-height:1.5;color:var(--ink)}
.cover-bar{position:absolute;left:230px;right:40px;top:608px;height:7px;background:var(--orange)}
/* toc */
.toc-frame{position:absolute;left:45px;top:60px;width:420px;height:600px;border:6px solid var(--orange)}
.toc-frame h2{font-family:"Exo 2",sans-serif;color:var(--orange);font-size:22px;margin:54px 0 22px 30px}
.toc-list{list-style:none;margin:0 30px;font-size:9px}
.toc-list li{padding:12px 0 8px;border-bottom:1px solid var(--grey-light)}
/* back */
.back .page{left:330px;background:var(--grey)}
.back-panel{position:absolute;left:60px;top:80px;width:420px;height:470px;background:#fff}
.back-brandbox{position:absolute;left:30px;top:30px;width:150px;height:140px;background:var(--orange);display:flex;flex-direction:column;align-items:center;justify-content:center}
.back-brandbox .brand{color:#fff;font-size:24px}
.back-brandbox .brand .dot{background:#fff}
.back-brandbox .brand-tag{color:#fff}
.back-photo-top{position:absolute;left:180px;top:30px;right:30px;height:140px;background:linear-gradient(135deg,#3a2a22,#8a5a3a 60%,#c9874f)}
.back-photo-bottom{position:absolute;left:30px;top:300px;right:30px;height:140px;background:linear-gradient(135deg,#e8e3dc,#c4b8a8 55%,#a36a3e)}
.back-title{position:absolute;left:30px;top:170px;width:250px;height:130px;background:#fff;padding:14px 18px}
.back-title .title-small{font-size:17px}
.back-title .title-big{font-size:30px;margin:2px 0}
.back-contact{position:absolute;left:60px;top:575px;width:420px;height:110px;background:#fff;padding:0 0 0 0}
.back-contact .label{display:inline-block;background:var(--orange);color:#fff;font-weight:700;font-size:10px;padding:4px 12px}
.back-contact .lines{padding:10px 14px;font-size:9.5px;line-height:1.6}
.back-contact .lines strong{font-weight:700}
.back-rule{position:absolute;left:60px;top:700px;width:300px;height:6px;background:var(--grey-light)}
</style>
</head>
<body>

<!-- Cover -->
<section class="sheet cover-sheet" style="top:0">
  <div class="page cover">
    <div style="position:absolute;left:30px;top:70px">
      <div class="brand" style="font-size:22px"><span class="dot"></span>VELTRA</div>
      <div class="brand-tag">Digital Solutions Group</div>
    </div>
    <div class="cover-photo" role="img" aria-label="Foto: Hand berührt eine leuchtende digitale Weltkarte mit Netzwerklinien in Blau"></div>
    <div class="cover-title-box">
      <div class="title-small">Sicherheit in</div>
      <div class="title-big">LoRaWAN<br>Netzen</div>
      <div class="title-small">ein Überblickt</div>
      <div class="cover-underline"></div>
    </div>
    <div class="cover-author">Autor: Marlene Kortwig, Geschäftsführerin<br>Veltra GmbH 6.5.2019</div>
    <div class="cover-bar"></div>
  </div>
</section>

<!-- Spread 1 -->
<section class="sheet spread" style="top:802px">
  <div class="page left">
    <div class="corner-block" style="right:70px;background:var(--orange)"></div>
    <div style="position:absolute;left:50px;top:50px;width:380px">
      <h2 style="font-family:'Exo 2',sans-serif;color:var(--orange);font-size:17px;margin-bottom:8px">Think Global Act Local</h2>
      <div class="body-text">
        <p>LoRaWAN steht für Long Range Wide Area Network und ist eine Funktechnologie zur Datenübertragung für Internet of Things Anwendungen. Sie wird zunehmend als Alternative zu Mobilfunk genutzt. Doch ist sie auch sicher? LoRaWAN kann sicher genutzt werden, wenn man die Schwachstellen kennt.</p>
        <p>Zur Beurteilung der Bedrohung durch Angreifer beschäftigt sich dieses Paper zunächst mit der Motivation und dem Schaden, den Angreifer anrichten können. Aufgrund der heute überwiegend regionalen Einsatzgebiete und der Limitierungen auf kleine Datenmengen ist LoRaWAN für Angreifer nicht der attraktivste Angriffspunkt. Die Infrastruktur dahinter jedoch kann mit verschiedenen Übertragungstechnologien genutzt und damit zum Angriffsziel sein.</p>
        <p>Der Schaden, der durch Angriffe bewirkt werden kann, muss für jeden Fall einzeln bewertet werden. Eine allgemeine Aussage für die Schadenshöhe kann nicht getroffen werden. Allgemein gilt nur, dass der Schaden bei einem Angriff auf die Things-Server in der Regel höher ist als der Schaden bei einem Angriff auf die LoRaWAN-Endgeräte.</p>
        <p>In diesem Artikel wird die LoRaWAN-Architektur beleuchtet, sowie die eingebauten Sicherheitsmechanismen. LoRaWAN bringt bereits sehr gute Sicherheitsmechanismen mit, wie z.B. AES-128 Nachrichtenverschlüsselung. Diese kann bis heute nicht geknackt werden, sofern sie korrekt und mit entsprechenden Vorsichtsmaßnahmen implementiert wird. Die Schwachstellen liegen eher im Bereich der Hardware, wenn nur weniger konkrete Standards für sichere Implementierung vorliegen. In Kombination mit unvorsichtigen Implementierungen, z.B. schlecht gesicherten Gateway oder Geräte-Standorten, können diese Schwachstellen ausgenutzt werden.</p>
      </div>
    </div>
    <div class="folio"><span>VELTRA</span><span class="rule"></span></div>
  </div>
  <div class="page right">
    <div class="corner-block" style="right:60px;background:var(--grey)"></div>
    <div class="body-text" style="position:absolute;left:60px;top:110px;width:400px">
      <p>Für eine sichere LoRaWAN-Implementierung ist es nicht notwendig, ein weiteres Verschlüsselungsprotokoll, wie z.B. TLS-Verschlüsselung, zu verwenden, da AES-128 selbst sicher ist und im Gesamtsystem ausreicht. Bei sicherheitskritischen Anwendungen wird ein zusätzlicher Schutz dennoch empfohlen. Notwendig sind ein gutes Schlüsselmanagement, professionelle Sicherheitsprozesse und gute physische Sicherheit zu implementieren, sowie das Netz redundant und sicher aufzubauen. Bei der Auswahl der Hardware, der Server, der Rechenzentren und der Software muss auf entsprechende Sicherheitsanforderungen geachtet werden. Die Kommunikation zwischen dem LoRaWAN und dem Rest der Infrastruktur muss entsprechend abgesichert werden.</p>
      <p>Es ist möglich, mit bestehender, nicht-proprietärer Technologie eine sichere, zuverlässige Internet of Things-Anwendung mit Kommunikation über LoRaWAN aufzubauen.</p>
    </div>
    <div class="folio"><span>VELTRA</span><span class="rule"></span></div>
  </div>
</section>

<!-- Spread 2 -->
<section class="sheet spread" style="top:1604px">
  <div class="page left">
    <div class="toc-frame">
      <h2>Inhalte</h2>
      <ol class="toc-list">
        <li>1. LoRaWAN – Eigenschaften und Anwendungsfälle</li>
        <li>2. Motivation für Angriffe auf LoRaWAN Netze – Nutzen des Angreifers</li>
        <li>3. Schaden durch Angriffe auf LoRaWAN-Netzwerke für den Nutzer oder Betreiber</li>
        <li>4. LoRaWAN 1.0 Architektur und Stack</li>
        <li>5. In LoRaWAN 1.0 eingebaute Sicherheitsmechanismen</li>
        <li>6. Schwachstellen und Angriffsarten</li>
        <li>7. Empfehlungen</li>
        <li>8. Schlussfolgerungen</li>
      </ol>
    </div>
    <div class="folio"><span>VELTRA</span><span class="rule"></span></div>
  </div>
  <div class="page right">
    <div class="corner-block" style="right:60px;background:var(--orange)"></div>
    <div style="position:absolute;left:55px;top:80px;width:420px">
      <div class="chapter-head"><span class="chapter-num">1.</span><h2 class="chapter-title">LoRaWAN – Eigenschaften und Anwendungsfälle</h2></div>
      <p class="lead">LoRaWAN ist eine Funktechnologie zur Übertragung von Maschinen-, Geräte- und Gebäudedaten. Seine Haupteigenschaften sind:</p>
      <ul class="bullets">
        <li>Hohe Reichweite – theoretisch bis zu 30km, praktisch im städtischen Bereich ca. 1-3km, im ländlichen Bereich mit freier Sicht bis zu 15km</li>
        <li>Sehr niedriger Stromverbrauch, d.h. die Lebensdauer der Endgeräte ist vor allem durch die Frequenz und Dauer der Datenübertragung bestimmt. Bei üblichen Anwendungen können Laufzeiten von bis zu 10 Jahren erreicht werden.</li>
        <li>Geringe Datenraten, d.h. es können nur geringe Datenmengen übertragen werden. Eine kontinuierliche Übertragung, wie einer Live-Videoüberwachung, ist nicht möglich.</li>
        <li>Freies Funkspektrum – LoRaWAN Netze dürfen frei aufgebaut und genutzt werden. Für das Funkspektrum fallen keine Nutzungsgebühren an, aber es gibt auch niemanden, der eine Garantie für die Übertragung übernimmt.</li>
        <li>Bidirektionale Datenübertragung, das heißt sowohl Auslesung von Daten als auch Steuerung von Aktoren sind möglich, mit den Limitierungen von Funknetzen allgemein.</li>
      </ul>
      <p class="lead">Durch diese Eigenschaften ergeben sich unter anderem folgende Anwendungsfälle (Beispiele):</p>
      <ul class="bullets">
        <li>Überwachung von Netzen und Infrastruktur, z.B. Strom-, Gas-, Wasser-, Fernwärme, Kanalnetze, Brücken, Straßen usw.</li>
      </ul>
    </div>
    <div class="folio"><span>VELTRA</span><span class="rule"></span></div>
  </div>
</section>

<!-- Spread 3 -->
<section class="sheet spread" style="top:2406px">
  <div class="page left">
    <div class="corner-block" style="right:70px;background:var(--grey)"></div>
    <div style="position:absolute;left:50px;top:50px;width:390px">
      <ul class="bullets">
        <li>Vollautomatische Zählerablesung</li>
        <li>Gebäudeüberwachung: Eindringlinge feststellen, Funktion von Geräten wie Klimaanlage etc., Raumklima, Raumbelegung überwachen</li>
        <li>Vorausschauende Wartung, z.B. von Klimaanlagen, bei denen der Zustand des Filters gemessen und daraus die Wartungsnotwendigkeit und gute Wartungsintervalle für individuelle Geräte gelernt werden</li>
        <li>Smart City Anwendungen wie Smart Parking, Routenoptimierung von Müllfahrzeugen, Beleuchtung usw.</li>
        <li>Smart Farming durch Überwachung von Bodeneigenschaften, Tracking und Gesundheitszustand der Tiere etc.</li>
      </ul>
      <div class="body-text" style="margin-top:6px">
        <p>Fahrzeug- oder Personenzählung, z.B. für Besucher, Durchgangsverkehr etc.</p>
        <p>Die erste Version von LoRaWAN – LoRaWAN 1.0 – wurde 2015 publiziert und wird seit 2015 kommerziell genutzt. Bereits 2017 wurde LoRaWAN 1.1 spezifiziert, ist aber bisher noch nicht weitreichend implementiert. Bisherige Server und Endgeräte basieren fast ausschließlich auf LoRaWAN 1.0. Deshalb bezieht sich dieses Paper auf LoRaWAN 1.0.</p>
        <p>Um eine vollständige Internet of Things-Anwendung aufzubauen und zu betreiben, werden neben LoRaWAN-Sensoren und Gateways weitere Komponenten benötigt. Dieses Paper beschäftigt sich im Schwerpunkt mit der Sicherheit der Kommunikation über LoRaWAN, am Rande mit der gesamten Architektur von Internet of Things-Anwendungen.</p>
      </div>
    </div>
    <div class="folio"><span>VELTRA</span><span class="rule"></span></div>
  </div>
  <div class="page right">
    <div class="corner-block" style="right:60px;background:var(--orange)"></div>
    <div style="position:absolute;left:55px;top:80px;width:420px">
      <div class="chapter-head"><span class="chapter-num">2.</span><h2 class="chapter-title">Motivation für Angriffe auf LoRaWAN Netze – Nutzen des Angreifers</h2></div>
      <div class="body-text" style="margin-top:16px">
        <p>Die erste Überlegung bei Sicherheitsbetrachtungen muss immer die Motivation von Angreifern sein. Welche Personengruppen oder Organisationen haben ein Interesse daran, ein System zu hacken, und welchen Vorteil erhoffen sie sich.</p>
        <p>Ebenfalls entscheidend ist, welchen Schaden sie mit einem Angriff anrichten können.</p>
        <p>Aus diesen beiden Überlegungen lässt sich ableiten, wieviel Aufwand in die Sicherheitsmaßnahmen eines Systems gesteckt werden muss.</p>
        <p>Aufgrund seiner Eigenschaften ist LoRaWAN eine beliebte Technologie im Versorgerbereich und Smart City-Umfeld. Die Motivationsbetrachtung bezieht sich daher in diesem Paper vor allem auf Versorger.</p>
        <p>Versorger können LoRaWAN grundsätzlich in drei Anwendungsbereichen nutzen:</p>
      </div>
      <ol class="alpha">
        <li><span>a.</span>Eigenbedarf – Steigerung der Effizienz der eigenen Abläufe. Hierzu zählen Themen wie Netz- und Infrastrukturüberwachung, Eindringlings-Detektion, Fernablesung von Zählerständen, Leckagen-Detektion, Gebäudemanagement usw.</li>
        <li><span>b.</span>Vermietung des Netzes an öffentliche oder private Unternehmen</li>
        <li><span>c.</span>Anbieten von kompletten Lösungen, z.B. für Smart City oder die Wohnungswirtschaft</li>
      </ol>
    </div>
    <div class="folio"><span>VELTRA</span><span class="rule"></span></div>
  </div>
</section>

<!-- Back cover -->
<section class="sheet back" style="top:3208px">
  <div class="page">
    <div class="back-panel">
      <div class="back-brandbox">
        <div class="brand"><span class="dot"></span>VELTRA</div>
        <div class="brand-tag">Digital Solutions Group</div>
      </div>
      <div class="back-photo-top" role="img" aria-label="Foto: Person am Laptop mit eingeblendeten Vernetzungssymbolen, warme Brauntöne"></div>
      <div class="back-title">
        <div class="title-small">Sicherheit in</div>
        <div class="title-big">LoRaWAN<br>Netzen</div>
        <div class="title-small">ein Überblickt</div>
      </div>
      <div class="back-photo-bottom" role="img" aria-label="Foto: Hände an einer Tastatur am hellen Arbeitsplatz"></div>
    </div>
    <div class="back-contact">
      <span class="label">Contact Us</span>
      <div class="lines">
        <strong>Veltra GmbH Lindenweg 12 · 40210 Düsseldorf</strong><br>
        T +49 211 5550190<br>
        E kontakt@veltra-digital.de
      </div>
    </div>
    <div class="back-rule"></div>
  </div>
</section>

</body>
</html>
```